KB Rubbish Removal Business Card

Hey,
I need a double sided business card designed for a rubbish removal business based in Australia. Logo is already chosen, similar colours preferred for both sides of the business card.

Details to include:

Front:

KB Rubbish Removal
Darren Holloway
Managing Director
Mobile: 0471 902 146
Email: darren@kbrubbishremoval.com.au
Website: kbrubbishremoval.com.au

Rear:

How did we do?
kbrubbishremoval.com.au/review

```html
<!DOCTYPE html>
<html lang="en">
<head>
<meta charset="utf-8">
<title>KB Rubbish Removal – Business Card</title>
<link rel="stylesheet" href="https://fonts.googleapis.com/css2?family=Montserrat:wght@700&family=Questrial&display=swap">
<style>
  :root {
    --bg: #2b2b2b;
    --card: #ffffff;
    --green-dark: #1c7a3a;
    --green-mid: #27993f;
    --green-light: #5fb446;
    --lime: #a6c639;
    --ink: #4a4a4a;
    --edge-shadow: #cfcfcf;
  }
  * { margin: 0; padding: 0; box-sizing: border-box; }
  html, body { width: 1200px; height: 900px; overflow: hidden; background: var(--bg); }
  .canvas { position: relative; width: 1200px; height: 900px; }

  .card {
    position: absolute; left: 250px; width: 700px; height: 400px;
    background: var(--card); overflow: hidden;
    box-shadow: 0 12px 30px rgba(0,0,0,.45);
  }
  .card--rear { top: 35px; }
  .card--front { top: 465px; }
  .card__waves { position: absolute; inset: 0; width: 700px; height: 400px; }

  .brand {
    position: absolute; display: flex; align-items: center; gap: 10px;
    font-family: "Montserrat", sans-serif; font-weight: 700; color: var(--green-mid);
  }
  .brand__dot { border-radius: 50%; background: var(--green-mid); flex: none; }

  /* rear */
  .rear__brand { left: 0; right: 0; top: 92px; justify-content: center; font-size: 18px; padding-left: 90px; }
  .rear__brand .brand__dot { width: 26px; height: 26px; }
  .rear__content { position: absolute; left: 90px; right: 0; top: 150px; text-align: center; }
  .rear__question { font-family: "Montserrat", sans-serif; font-weight: 700; font-size: 24px; color: var(--green-dark); }
  .rear__url { font-family: "Questrial", sans-serif; font-size: 27px; color: var(--lime); margin-top: 4px; }
  .rear__rule { width: 380px; height: 1.5px; margin: 16px auto 18px; background: linear-gradient(90deg, transparent, var(--green-mid), transparent); }
  .rear__heading { font-family: "Montserrat", sans-serif; font-weight: 700; font-size: 15px; color: var(--green-dark); letter-spacing: .5px; }
  .rear__services { font-family: "Questrial", sans-serif; font-size: 19px; color: var(--lime); margin-top: 14px; letter-spacing: .5px; }
  .rear__services .sep { color: var(--green-light); margin: 0 6px; }

  /* front */
  .front__brand { left: 40px; top: 270px; width: 240px; font-size: 20px; line-height: 1.2; }
  .front__brand .brand__dot { width: 56px; height: 56px; }
  .front__details { position: absolute; left: 330px; top: 228px; font-family: "Questrial", sans-serif; color: var(--ink); }
  .front__name { font-family: "Montserrat", sans-serif; font-weight: 700; font-size: 25px; color: var(--green-mid); letter-spacing: .3px; }
  .front__role { font-size: 19px; margin-top: 2px; }
  .contact { list-style: none; margin-top: 18px; font-size: 17.5px; }
  .contact li { display: flex; align-items: center; gap: 8px; margin-bottom: 5px; }
  .contact svg { width: 16px; height: 16px; flex: none; fill: var(--green-mid); }
</style>
</head>
<body>
<div class="canvas">

  <!-- Rear side -->
  <section class="card card--rear" aria-label="Business card rear">
    <svg class="card__waves" viewBox="0 0 700 400" aria-hidden="true">
      <defs>
        <linearGradient id="rearGreen" x1="0" y1="1" x2="1" y2="0">
          <stop offset="0" stop-color="#5fb446"/>
          <stop offset=".5" stop-color="#27993f"/>
          <stop offset="1" stop-color="#1c7a3a"/>
        </linearGradient>
      </defs>
      <path d="M0,0 H700 V38 C610,38 560,66 470,56 C380,46 300,36 250,120 C205,195 150,262 0,262 Z" fill="#cfcfcf" transform="translate(0,6)"/>
      <path d="M0,0 H700 V38 C610,38 560,66 470,56 C380,46 300,36 250,120 C205,195 150,262 0,262 Z" fill="url(#rearGreen)"/>
    </svg>
    <div class="brand rear__brand"><span class="brand__dot"></span>KB Rubbish Removal</div>
    <div class="rear__content">
      <p class="rear__question">How did we do?</p>
      <p class="rear__url">kbrubbishremoval.com.au/review</p>
      <div class="rear__rule"></div>
      <p class="rear__heading">WHAT WE TAKE</p>
      <p class="rear__services">DOMESTIC WASTE<span class="sep">✦</span>OFFICE WASTE<span class="sep">✦</span>HEAVY WASTE</p>
    </div>
  </section>

  <!-- Front side -->
  <section class="card card--front" aria-label="Business card front">
    <svg class="card__waves" viewBox="0 0 700 400" aria-hidden="true">
      <defs>
        <linearGradient id="frontGreen" x1="0" y1="1" x2="1" y2="0">
          <stop offset="0" stop-color="#5fb446"/>
          <stop offset=".5" stop-color="#27993f"/>
          <stop offset="1" stop-color="#1c7a3a"/>
        </linearGradient>
      </defs>
      <path d="M0,0 H700 V52 C620,52 560,84 480,94 C380,106 330,66 272,112 C222,152 200,212 0,216 Z" fill="#cfcfcf" transform="translate(0,6)"/>
      <path d="M0,0 H700 V52 C620,52 560,84 480,94 C380,106 330,66 272,112 C222,152 200,212 0,216 Z" fill="url(#frontGreen)"/>
    </svg>
    <div class="brand front__brand"><span class="brand__dot"></span>KB Rubbish Removal</div>
    <div class="front__details">
      <h1 class="front__name">DARREN HOLLOWAY</h1>
      <p class="front__role">Managing Director</p>
      <ul class="contact">
        <li><svg viewBox="0 0 16 16" aria-hidden="true"><path d="M4 1h8a1 1 0 0 1 1 1v12a1 1 0 0 1-1 1H4a1 1 0 0 1-1-1V2a1 1 0 0 1 1-1zm1 2v9h6V3z"/></svg>0471 902 146</li>
        <li><svg viewBox="0 0 16 16" aria-hidden="true"><path d="M1 4h14v9H1zm1.5 1.2L8 9l5.5-3.8V5h-11z"/></svg>darren@kbrubbishremoval.com.au</li>
        <li><svg viewBox="0 0 16 16" aria-hidden="true"><circle cx="8" cy="8" r="7"/></svg>kbrubbishremoval.com.au</li>
      </ul>
    </div>
  </section>

</div>
</body>
</html>
```